Falcrest security business card

Looking for a business card for my security company

Target Market(s)

Security

Industry/Entity Type

Security

Contact Information for Business Card

Name - Gil Marston. Title - General manager - direct 314 862.4490 website www. falcrestsecurityservices.example email - gil@ falcrestsecurityservices.example

Requirements
Must have
• Logo attached

```html
<!DOCTYPE html>
<html lang="en">
<head>
<meta charset="utf-8">
<title>Falcrest Security Services — Business Card</title>
<link href="https://fonts.googleapis.com/css2?family=Lato:wght@400;700&display=swap" rel="stylesheet">
<style>
  :root {
    --backdrop: #9a9b9a;
    --card: #151515;
    --card-edge: #1c1c1c;
    --gold: #c9a24a;
    --gold-line: #8a6d2f;
    --ink-light: #f2f2f2;
  }
  * { box-sizing: border-box; margin: 0; padding: 0; }
  html, body { width: 1200px; height: 1200px; overflow: hidden; }
  body {
    background: var(--backdrop);
    font-family: "Lato", sans-serif;
    position: relative;
  }
  .card {
    position: absolute;
    left: 222px;
    width: 755px;
    height: 463px;
    background: radial-gradient(ellipse at 50% 45%, var(--card-edge), var(--card) 70%);
  }
  .card--front { top: 105px; }
  .card--back { top: 630px; }

  .brand-name {
    position: absolute;
    color: var(--gold);
    font-weight: 700;
    text-transform: uppercase;
    white-space: nowrap;
    transform: translate(-50%, -50%);
  }
  .card--front .brand-name { left: 180px; top: 231px; font-size: 44px; letter-spacing: 1px; }
  .card--back .brand-name { left: 377px; top: 231px; font-size: 100px; letter-spacing: 2px; }

  .divider {
    position: absolute;
    left: 330px;
    top: 145px;
    width: 1px;
    height: 172px;
    background: var(--gold-line);
  }
  .contact { position: absolute; left: 352px; top: 140px; }
  .contact__name { color: var(--gold); font-size: 31px; font-weight: 400; line-height: 1.1; }
  .contact__title { color: var(--ink-light); font-size: 21px; font-weight: 700; margin-top: 4px; }
  .contact__list { list-style: none; margin-top: 32px; }
  .contact__item {
    display: flex;
    align-items: center;
    gap: 10px;
    color: var(--ink-light);
    font-size: 20px;
    height: 32px;
  }
  .contact__icon { width: 22px; height: 22px; flex: none; }
</style>
</head>
<body>
  <section class="card card--front" aria-label="Business card front">
    <div class="brand-name">Falcrest</div>
    <div class="divider"></div>
    <div class="contact">
      <h1 class="contact__name">Gil Marston</h1>
      <p class="contact__title">General manager</p>
      <ul class="contact__list">
        <li class="contact__item">
          <svg class="contact__icon" viewBox="0 0 24 24" aria-hidden="true">
            <path d="M3 9c0-3 4-5 9-5s9 2 9 5l-3 1-2-3H8L6 10z" fill="#c9a24a"/>
            <rect x="5" y="11" width="14" height="9" rx="2" fill="#c9a24a"/>
            <circle cx="12" cy="15.5" r="2.5" fill="#151515"/>
          </svg>
          314 862.4490
        </li>
        <li class="contact__item">
          <svg class="contact__icon" viewBox="0 0 24 24" aria-hidden="true">
            <rect x="2" y="5" width="17" height="12" fill="#c9a24a"/>
            <path d="M2 5l8.5 7L19 5" stroke="#151515" stroke-width="1.5" fill="none"/>
            <circle cx="18" cy="17" r="4.5" fill="#c9a24a" stroke="#151515" stroke-width="1"/>
            <path d="M16 17l1.5 1.5 2.5-3" stroke="#151515" stroke-width="1.5" fill="none"/>
          </svg>
          gil@ falcrestsecurityservices.example
        </li>
        <li class="contact__item">
          <svg class="contact__icon" viewBox="0 0 24 24" aria-hidden="true">
            <g fill="none" stroke="#c9a24a" stroke-width="1.5">
              <circle cx="12" cy="12" r="9"/>
              <ellipse cx="12" cy="12" rx="4" ry="9"/>
              <path d="M3 12h18M4.5 7.5h15M4.5 16.5h15"/>
            </g>
          </svg>
          www. falcrestsecurityservices.example
        </li>
      </ul>
    </div>
  </section>

  <section class="card card--back" aria-label="Business card back">
    <div class="brand-name">Falcrest</div>
  </section>
</body>
</html>
```